Business Cards for company that supports physicians that do medical research

Need to create a business card for Nerivale Studies (www.nerivalestudies.example), a company devoted to supporting physicians who conduct medical research. The form of the card should match the message of research and information quest. I have provided the logo of the company as an uploaded file. Designs should be simple and slick aimed at very high end clients.

Target Market(s)

Medical doctors that are also researchers

Industry/Entity Type

Medical

Contact Information for Business Card

Should feature logo and fields for personal info:
Name/title
Phone /email

Font styles to use
Serif
Sans Serif

Requirements
Must have
• Nerivale logo and fields for personal info:
• Name: Corwin Abbatelli
• Title: VP Research and Senior Analyst
• Phone: 555-203-7416
• email: info@nerivalestudies.example
Nice to have
• Interesting cards that I've seen:
• 1- all black/charcoal or very dark background
• 2- Plastic - semi-transparent
• 3- non-standard height-width ratios
• 4- Functional cards -- USB drive incorporated
Should not have
• Too busy; needs to stay very simple

```html
<!DOCTYPE html>
<html lang="en">
<head>
<meta charset="utf-8">
<title>Nerivale Studies — Business Card</title>
<link rel="stylesheet" href="https://fonts.googleapis.com/css2?family=Source+Sans+3:wght@400;600&display=swap">
<style>
  :root {
    --backdrop: #a8a6a6;
    --card: #2d2f32;
    --card-light: #3a3c40;
    --white: #f4f4f4;
    --soft-white: #e2e3e5;
    --blue: #2a8ad6;
    --band-blue: #3a76b6;
    --green: #33a544;
  }
  html, body {
    margin: 0;
    width: 1200px;
    height: 1200px;
    overflow: hidden;
    background: var(--backdrop);
    font-family: "Source Sans 3", sans-serif;
  }
  .card {
    position: absolute;
    width: 712px;
    height: 418px;
    border-radius: 28px;
    overflow: hidden;
    background: var(--card);
  }
  .card-front { left: 238px; top: 118px; }
  .card-back { left: 231px; top: 645px; }
  .card-photo {
    position: absolute;
    inset: 0;
    background: radial-gradient(ellipse at 78% 35%, var(--card-light) 0%, var(--card) 55%, #282a2d 100%);
  }
  .brand-name {
    position: absolute;
    color: var(--white);
    font-weight: 400;
    text-align: center;
    line-height: 1;
  }
  .brand-name .word-main { display: block; font-size: 84px; letter-spacing: 1px; }
  .brand-name .word-sub { display: block; font-size: 36px; letter-spacing: 11px; margin-top: 14px; }
  .brand-dot {
    position: absolute;
    width: 22px; height: 22px;
    border-radius: 50%;
    background: var(--green);
  }
  .card-front .brand-name { left: 0; right: 0; top: 150px; }
  .card-front .brand-dot { left: 345px; top: 120px; }
  .card-back .brand-name { left: 62px; top: 112px; text-align: left; }
  .card-back .brand-name .word-main { font-size: 68px; }
  .card-back .brand-name .word-sub { font-size: 32px; letter-spacing: 9px; margin-top: 18px; }
  .card-back .brand-dot { left: 64px; top: 84px; width: 18px; height: 18px; }
  .contact {
    position: absolute;
    left: 413px;
    top: 120px;
    color: var(--soft-white);
  }
  .contact-name { font-size: 24px; font-weight: 600; color: var(--blue); letter-spacing: 0.5px; margin: 0; }
  .contact-title { font-size: 17px; margin: 2px 0 20px; }
  .contact-line { display: flex; align-items: center; font-size: 18px; margin: 0 0 2px; }
  .contact-line svg { width: 17px; height: 14px; margin-right: 15px; fill: var(--blue); }
  .footer-band { position: absolute; left: 0; bottom: 0; width: 712px; height: 58px; }
  .footer-url {
    position: absolute;
    left: 413px;
    bottom: 17px;
    color: var(--white);
    font-size: 18px;
    letter-spacing: 0.3px;
  }
</style>
</head>
<body>
  <section class="card card-front">
    <div class="card-photo" role="img" aria-label="Dimmed photo of a stethoscope resting on a desk with a keyboard"></div>
    <span class="brand-dot"></span>
    <div class="brand-name"><span class="word-main">Nerivale</span><span class="word-sub">STUDIES</span></div>
  </section>

  <section class="card card-back">
    <div class="card-photo" role="img" aria-label="Dimmed photo of a stethoscope resting on a desk with a keyboard"></div>
    <span class="brand-dot"></span>
    <div class="brand-name"><span class="word-main">Nerivale</span><span class="word-sub">STUDIES</span></div>
    <div class="contact">
      <p class="contact-name">Corwin Abbatelli</p>
      <p class="contact-title">VP Research &amp; Senior Analyst</p>
      <p class="contact-line">
        <svg viewBox="0 0 17 14"><path d="M1 4 Q8.5 -1 16 4 L14 6 L11.5 4.5 L11.5 3 Q8.5 2 5.5 3 L5.5 4.5 L3 6 Z M4 7 L13 7 L15 13 L2 13 Z"/></svg>
        555-203-7416
      </p>
      <p class="contact-line">
        <svg viewBox="0 0 17 14"><path d="M0 1 L17 1 L8.5 8 Z M0 3 L8.5 10 L17 3 L17 13 L0 13 Z"/></svg>
        info@nerivalestudies.example
      </p>
    </div>
    <svg class="footer-band" viewBox="0 0 712 58" preserveAspectRatio="none">
      <polygon points="0,30 362,30 352,58 0,58" fill="var(--band-blue)"/>
      <polygon points="376,0 712,0 712,58 350,58" fill="var(--green)"/>
    </svg>
    <span class="footer-url">www.nerivalestudies.example</span>
  </section>
</body>
</html>
```